KVR PROTECTIVE COATINGS BROCHURE

To design a 4 page A4 brochure of protective coating system for steel and concrete infrastructure with industrial , telecoms and oil & gas markets.

brochure title; Inorganic siloxane protective coatings for steel and concrete infrastructure
sub title - Non-isocyanate (NISO) Coatings
Products:
- KVR 300 1K solvent free inorganic tintable finish coat for ultra UV durability
- KVR 300 DM 1K solvent free clear coat for protection of steel and concrete substrates, anti graffiti, highly UV resistant
- KVR BASEGUARD 2K epoxy hybrid anti corrosion coating for steel
- KVR TILEMAX 1K glass flake single pack high abrasion resistant coating
- KVR DURAMETAL 1K single component siloxane zinc anti-corrosion coating
- KVR TANO 1K single component intermediate anti-corrosion coating
- KVR 470 2K two component epoxy-siloxane hybrid durable tintable top coat
- KVR DECKSHIELD 2K two component, chemical resistant, durable floor coating.
- KVR STONEWEAR 2K two component ceramically filled epoxy for high abrasion resistance.

use good clear images of markets sectors (oil&gas, Telecoms, Industrial)
use icons for low VOC, low toxicity, Green, high weathering resistance, chemical resistance, maintenance friendly, environment friendly, non-isocyanate.

Table of primers and top coats in attachment, please use images within document about tinting products

Company Info
Tel +44 (0) 1632 960518
Email sales@tq-hr.example
Address 7-8 Larkwell Meadow Trade Park, Fennick Lane, United Kingdom
web www.tq-hr.example

Target Market(s)

Protective Coatings

Requirements
Must have
• Clear images of target markets and good layout of information provided

```html
<!DOCTYPE html>
<html lang="en">
<head>
<meta charset="utf-8">
<title>KVR Protective Coatings Brochure</title>
<link rel="stylesheet" href="https://fonts.googleapis.com/css2?family=Lexend:wght@300;400;600;700&display=swap">
<style>
:root{
  --navy:#0f2c45;
  --navy-deep:#0a2138;
  --blue:#1f5fb4;
  --sky:#3fa9e6;
  --sky-pale:#cfe7f6;
  --paper:#f5f6f7;
  --stage:#e4e6e8;
  --ink:#1d2733;
  --muted:#5a6673;
  --rule:#c9d0d7;
}
*{box-sizing:border-box;margin:0;padding:0}
html,body{width:900px;height:1200px;overflow:hidden;background:var(--stage);font-family:"Lexend",sans-serif;color:var(--ink)}
.sheet{position:relative;width:900px;height:1200px;padding:4px 30px}
.spread{display:flex;width:840px;height:594px;box-shadow:0 6px 18px rgba(0,0,0,.18)}
.spread + .spread{margin-top:4px}
.page{position:relative;width:420px;height:594px;background:var(--paper);overflow:hidden}

/* back cover */
.back-band{position:absolute;left:0;top:0;width:100%;height:22px;background:linear-gradient(90deg,var(--navy-deep),var(--navy))}
.contact{position:absolute;left:0;top:105px;width:440px;text-align:center;font-size:10.5px;line-height:1.6;color:var(--ink)}
.contact .brand-name{font-weight:700;color:var(--blue);font-size:13px;margin-bottom:6px;display:flex;align-items:center;justify-content:center;gap:6px}
.contact .brand-dot{width:10px;height:10px;border-radius:50%;background:var(--sky)}
.contact strong{font-weight:700}
.photo-offshore{position:absolute;left:0;bottom:0;width:100%;height:310px;background:linear-gradient(180deg,rgba(245,246,247,0) 0%,#c9b9a0 22%,#e9b36c 42%,#f3c57f 50%,#3e7ea8 70%,#14547f 100%)}

/* front cover */
.front-logo{position:absolute;right:34px;top:40px;display:flex;align-items:center;gap:8px}
.front-logo .brand-dot{width:16px;height:16px;border-radius:50%;background:var(--sky)}
.front-logo .brand-name{font-size:22px;font-weight:700;color:var(--blue);line-height:1}
.tagline{position:absolute;right:34px;top:68px;font-size:11px;font-weight:300;color:var(--muted);letter-spacing:.5px}
.accent-top{position:absolute;left:74px;top:120px;width:346px;height:24px;background:linear-gradient(90deg,var(--sky-pale),var(--sky))}
.photo-silos{position:absolute;left:108px;top:144px;width:312px;height:260px;background:linear-gradient(180deg,#c7d2dc 0%,#9fb0c0 38%,#7f93a6 58%,#6c9a3c 72%,#8fc04a 100%)}
.title-block{position:absolute;left:28px;top:330px;width:270px;height:232px;background:var(--navy);padding:30px 22px 0}
.title{font-size:21px;line-height:1.18;color:#fff;font-weight:300}
.title .hl{color:var(--sky);font-weight:600}
.title b{font-weight:700}
.subtitle{margin-top:10px;font-size:12.5px;font-weight:300;color:#d8e3ec}
.web{position:absolute;left:0;bottom:18px;width:100%;text-align:center;font-size:10.5px;color:#fff;font-weight:400}
.accent-bottom{position:absolute;left:298px;top:404px;width:122px;height:110px;background:linear-gradient(135deg,var(--sky-pale),var(--sky))}

/* products page */
.section-band{position:absolute;left:0;top:0;width:100%;height:46px;background:linear-gradient(90deg,var(--navy),var(--navy-deep))}
.section-title{position:absolute;right:34px;top:12px;font-size:17px;font-style:italic;font-weight:600;color:#fff}
.product-grid{position:absolute;left:18px;top:64px;display:grid;grid-template-columns:repeat(3,124px);gap:10px 8px}
.product{position:relative;height:162px}
.product-photo{position:absolute;inset:0 0 36px 0}
.product-label{position:absolute;left:0;right:10px;bottom:0;height:84px;background:var(--blue);color:#fff;padding:7px 8px;text-align:center}
.product-name{font-size:10px;font-weight:700;line-height:1.15}
.product-desc{margin-top:3px;font-size:7.2px;line-height:1.3;font-weight:300}
.ph-a{background:linear-gradient(135deg,#d7dde3,#8a9aa9)}
.ph-b{background:linear-gradient(135deg,#e6d4c4,#8fa6bb)}
.ph-c{background:linear-gradient(135deg,#b5c3cf,#57697c)}
.ph-d{background:linear-gradient(135deg,#5e8fc2,#e2e8f0)}
.ph-e{background:linear-gradient(135deg,#cfd6de,#2e5d98)}
.ph-f{background:linear-gradient(135deg,#dfe6ec,#7390b0)}
.ph-g{background:linear-gradient(135deg,#e4e8ec,#c06a3a)}
.ph-h{background:linear-gradient(135deg,#d0d6dc,#6c7580)}
.ph-i{background:linear-gradient(135deg,#e6eaee,#4f9aa2)}

/* data page */
.photo-plant{position:absolute;left:0;top:0;width:100%;height:212px;background:linear-gradient(120deg,#e8edf2 0%,#9bb4cf 30%,#2f5f9e 60%,#1c4a88 100%)}
.benefits{position:absolute;right:14px;top:22px;width:230px;display:grid;grid-template-columns:repeat(4,1fr);gap:12px 4px}
.benefit{text-align:center;color:#fff;font-size:7px;line-height:1.2}
.benefit svg{display:block;margin:0 auto 3px}
.table-heading{font-size:13px;font-weight:700;color:var(--ink);margin:0 0 4px}
.table-wrap{position:absolute;left:22px;width:376px}
.table-main{top:222px}
.table-tint{top:410px}
table{width:100%;border-collapse:collapse;font-size:7px;line-height:1.2}
th{background:var(--blue);color:#fff;font-weight:600;text-align:left;padding:2px 4px}
td{padding:1.6px 4px;border-bottom:1px solid var(--rule)}
td.num,th.num{text-align:center}
.ral-chart{position:absolute;left:22px;top:498px;width:230px;height:80px;background:linear-gradient(90deg,#e8c36a,#d6643e,#a8425a,#6a5c9c,#3d7fb8,#4c9b68,#8c8a7a)}
.ral-label{position:absolute;left:262px;top:530px;font-size:16px;font-weight:700;color:var(--ink)}
</style>
</head>
<body>
<div class="sheet">

  <section class="spread">
    <article class="page back-cover">
      <div class="back-band"></div>
      <div class="contact">
        <div class="brand-name"><span class="brand-dot"></span>Tenqor Resins</div>
        <strong>+44 (0) 1632 960518</strong><br>
        <strong>sales@tq-hr.example</strong><br>
        7-8 Larkwell Meadow Trade Park,<br>
        Fennick Lane, United Kingdom<br>
        www.tq-hr.example
      </div>
      <div class="photo-offshore" role="img" aria-label="Offshore oil and gas platform at sea during sunset"></div>
    </article>

    <article class="page front-cover">
      <div class="front-logo"><span class="brand-dot"></span><span class="brand-name">Tenqor Resins</span></div>
      <div class="tagline">Inorganic Innovation</div>
      <div class="accent-top"></div>
      <div class="photo-silos" role="img" aria-label="Steel storage silos beside a green field under a cloudy sky"></div>
      <div class="accent-bottom"></div>
      <div class="title-block">
        <h1 class="title"><span class="hl">Inorganic siloxane</span> protective coatings for <b>steel</b> and <b>concrete infrastructure</b></h1>
        <p class="subtitle">Non-isocyanate (NISO) Coatings</p>
        <p class="web">www.tq-hr.example</p>
      </div>
    </article>
  </section>

  <section class="spread">
    <article class="page products-page">
      <div class="section-band"></div>
      <h2 class="section-title">Products</h2>
      <div class="product-grid">
        <div class="product"><div class="product-photo ph-a" role="img" aria-label="Coated steel surface"></div><div class="product-label"><div class="product-name">KVR 300 1K</div><div class="product-desc">solvent free inorganic tintable finish coat for ultra UV durability</div></div></div>
        <div class="product"><div class="product-photo ph-b" role="img" aria-label="Concrete building under construction"></div><div class="product-label"><div class="product-name">KVR 300 DM 1K</div><div class="product-desc">solvent free clear coat for protection of steel and concrete substrates, anti graffiti, highly UV resistant</div></div></div>
        <div class="product"><div class="product-photo ph-c" role="img" aria-label="Worker coating steel structure"></div><div class="product-label"><div class="product-name">KVR BASEGUARD 2K</div><div class="product-desc">epoxy hybrid anti corrosion coating for steel</div></div></div>
        <div class="product"><div class="product-photo ph-d" role="img" aria-label="Glass flake close-up"></div><div class="product-label"><div class="product-name">KVR TILEMAX 1K</div><div class="product-desc">glass flake single pack high abrasion resistant coating</div></div></div>
        <div class="product"><div class="product-photo ph-e" role="img" aria-label="Blue coated metal pipe"></div><div class="product-label"><div class="product-name">KVR DURAMETAL 1K</div><div class="product-desc">single component siloxane zinc anti-corrosion coating</div></div></div>
        <div class="product"><div class="product-photo ph-f" role="img" aria-label="Spray application of coating"></div><div class="product-label"><div class="product-name">KVR TANO 1K</div><div class="product-desc">single component intermediate anti-corrosion coating</div></div></div>
        <div class="product"><div class="product-photo ph-g" role="img" aria-label="Painter working on an industrial roof"></div><div class="product-label"><div class="product-name">KVR 470 2K</div><div class="product-desc">two component epoxy-siloxane hybrid durable tintable top coat</div></div></div>
        <div class="product"><div class="product-photo ph-h" role="img" aria-label="Floor coating being applied"></div><div class="product-label"><div class="product-name">KVR DECKSHIELD 2K</div><div class="product-desc">two component, chemical resistant, durable floor coating</div></div></div>
        <div class="product"><div class="product-photo ph-i" role="img" aria-label="Gloved hands mixing a ceramic filled coating"></div><div class="product-label"><div class="product-name">KVR STONEWEAR 2K</div><div class="product-desc">two component ceramically filled epoxy for high abrasion resistance</div></div></div>
      </div>
    </article>

    <article class="page data-page">
      <div class="photo-plant" role="img" aria-label="Coating tin in front of an industrial plant in blue tones"></div>
      <div class="benefits">
        <div class="benefit"><svg width="26" height="26" viewBox="0 0 26 26"><circle cx="13" cy="13" r="12" fill="none" stroke="#fff" stroke-width="1.2"/><path d="M8 17c0-6 4-9 10-9-1 6-4 9-10 9z" fill="none" stroke="#fff" stroke-width="1.2"/></svg>Low VOC</div>
        <div class="benefit"><svg width="26" height="26" viewBox="0 0 26 26"><circle cx="13" cy="13" r="12" fill="none" stroke="#fff" stroke-width="1.2"/><path d="M8 8l10 10M18 8L8 18" stroke="#fff" stroke-width="1.2"/></svg>Low Toxicity</div>
        <div class="benefit"><svg width="26" height="26" viewBox="0 0 26 26"><circle cx="13" cy="13" r="12" fill="none" stroke="#fff" stroke-width="1.2"/><path d="M13 19V9M13 13l-4-3M13 12l4-3" stroke="#fff" stroke-width="1.2" fill="none"/></svg>Green</div>
        <div class="benefit"><svg width="26" height="26" viewBox="0 0 26 26"><circle cx="13" cy="13" r="12" fill="none" stroke="#fff" stroke-width="1.2"/><circle cx="13" cy="13" r="4" fill="none" stroke="#fff" stroke-width="1.2"/><path d="M13 5v3M13 18v3M5 13h3M18 13h3" stroke="#fff" stroke-width="1.2"/></svg>High Weathering Resistance</div>
        <div class="benefit"><svg width="26" height="26" viewBox="0 0 26 26"><circle cx="13" cy="13" r="12" fill="none" stroke="#fff" stroke-width="1.2"/><path d="M11 7h4M12 7v5l-4 7h10l-4-7V7" stroke="#fff" stroke-width="1.2" fill="none"/></svg>Chemical Resistance</div>
        <div class="benefit"><svg width="26" height="26" viewBox="0 0 26 26"><circle cx="13" cy="13" r="12" fill="none" stroke="#fff" stroke-width="1.2"/><path d="M9 17l6-6M15 11l2-3 2 2-3 2" stroke="#fff" stroke-width="1.2" fill="none"/></svg>Maintenance Friendly</div>
        <div class="benefit"><svg width="26" height="26" viewBox="0 0 26 26"><circle cx="13" cy="13" r="12" fill="none" stroke="#fff" stroke-width="1.2"/><path d="M8 13a5 5 0 0 1 9-3M18 13a5 5 0 0 1-9 3" stroke="#fff" stroke-width="1.2" fill="none"/></svg>Environment Friendly</div>
        <div class="benefit"><svg width="26" height="26" viewBox="0 0 26 26"><circle cx="13" cy="13" r="12" fill="none" stroke="#fff" stroke-width="1.2"/><path d="M9 14l3 3 6-7" stroke="#fff" stroke-width="1.4" fill="none"/></svg>Non-Isocyanate</div>
      </div>

      <div class="table-wrap table-main">
        <h3 class="table-heading">1 and 2 Component Siloxane based Coatings:</h3>
        <table>
          <thead><tr><th>Product</th><th class="num">Components</th><th>Functionality</th><th>Chemistry</th><th class="num">DFT (µm)</th></tr></thead>
          <tbody>
            <tr><td>KVR TANO 1K</td><td class="num">1</td><td>Anti-corrosion Primer</td><td>Siloxane</td><td class="num">150 - 200</td></tr>
            <tr><td>KVR DURAMETAL 1K</td><td class="num">1</td><td>Anti-corrosion Primer</td><td>Siloxane-Zinc</td><td class="num">75 - 100</td></tr>
            <tr><td>KVR TILEMAX 1K</td><td class="num">1</td><td>Abrasion resistant Primer</td><td>Siloxane-Ceramic</td><td class="num">200 - 250</td></tr>
            <tr><td>KVR 300 1K</td><td class="num">1</td><td>Durable Topcoat</td><td>Siloxane</td><td class="num">75 - 150</td></tr>
            <tr><td>KVR 300 DM 1K</td><td class="num">1</td><td>Durable clear coat (anti-graffiti)</td><td>Siloxane</td><td class="num">25 - 50</td></tr>
            <tr><td>KVR BASEGUARD 2K</td><td class="num">2</td><td>Anti-corrosion Primer</td><td>Epoxy-Hybrid</td><td class="num">100 - 200</td></tr>
            <tr><td>KVR STONEWEAR 2K</td><td class="num">2</td><td>Abrasion resistant Primer</td><td>Epoxy-Ceramic</td><td class="num">200 - 250</td></tr>
            <tr><td>KVR 470 2K</td><td class="num">2</td><td>Durable Topcoat</td><td>Siloxane-Hybrid</td><td class="num">75 - 150</td></tr>
            <tr><td>KVR DECKSHIELD 2K</td><td class="num">2</td><td>UV durable floor coating</td><td>Siloxane-Hybrid</td><td class="num">200 - 250</td></tr>
          </tbody>
        </table>
      </div>

      <div class="table-wrap table-tint">
        <h3 class="table-heading">Tintable Top Coats:</h3>
        <table>
          <thead><tr><th>Product</th><th class="num">Components</th><th>Functionality</th><th>Chemistry</th><th class="num">DFT (µm)</th></tr></thead>
          <tbody>
            <tr><td>KVR 300 1K</td><td class="num">1</td><td>Durable Topcoat</td><td>RAL, BS &amp; Custom</td><td class="num">75 - 150</td></tr>
            <tr><td>KVR 470 2K</td><td class="num">2</td><td>Durable Topcoat</td><td>RAL, BS &amp; Custom</td><td class="num">75 - 150</td></tr>
            <tr><td>KVR DECKSHIELD 2K</td><td class="num">2</td><td>UV durable floor coating</td><td>RAL, BS &amp; Custom</td><td class="num">200 - 250</td></tr>
          </tbody>
        </table>
      </div>

      <div class="ral-chart" role="img" aria-label="RAL colour swatch chart of available tints"></div>
      <div class="ral-label">RAL</div>
    </article>
  </section>

</div>
</body>
</html>
```